Wordpress design for lovely french B&B - Mas des Ormeaux

We need a Wordpress design for a B&B located in eastern France.
The current website (designed by the previous owners) is here: http://www.masdesormeaux-exemple.fr. But it's not what we want, it has some photos so you can have a look at what it looks like.
New photos will be taken.

The new design should be fresh, modern and engaging and reflect the fact that it is a lovely B&B with 5 rooms. It is located in a lovely french village, close to the german and swiss border. It is perfectly located, close to the city, stores and highways, and also close to the country side.

The website should be able to describe each of the 5 rooms (1 page per room, with photos, description, price and booking).
The website should also have a pages to display the surrounding activities (one page with country side activities and one page with city activities) and also have a map for directions as well as a contact page with a form.
We will include a wordpress booking plugin so people can book online.

Target Market(s)

People visiting the french country side

Industry/Entity Type

Online

Logo Text

Le Mas des Ormeaux

Font styles to use
Script

Requirements
Must have
• Should feel like it's in the country side, but also feel like it's a little bit of luxury but not too much
Should not have
• I used B&B term to make it understandable, but it should not use the term B&B. It should use the french term "Gîte"

```html
<!DOCTYPE html>
<html lang="fr">
<head>
<meta charset="utf-8">
<title>Le Mas des Ormeaux – Gîte</title>
<link href="https://fonts.googleapis.com/css2?family=Open+Sans:wght@400;600;700&display=swap" rel="stylesheet">
<style>
:root{
  --plum:#5e1a4d;
  --plum-dark:#3e0c33;
  --plum-deep:#2c0824;
  --ink:#222;
  --muted:#777;
  --band:#ececec;
  --white:#fff;
  --green:#5f8f2e;
  --orange:#c8641e;
  --blue:#2b6a9e;
}
*{box-sizing:border-box;margin:0;padding:0}
html,body{width:711px;height:1200px;overflow:hidden}
body{font-family:"Open Sans",Arial,sans-serif;color:var(--ink);background:var(--white);font-size:9px}
.site-header{height:45px;display:flex;align-items:stretch;justify-content:space-between;padding-left:26px;background:var(--white)}
.brand{display:flex;align-items:center;font-weight:600;font-size:17px;color:var(--plum-dark)}
.main-nav{display:flex;background:var(--plum);margin-right:0;align-self:stretch}
.main-nav a{display:flex;align-items:center;padding:0 10px;color:var(--white);font-size:8.5px;text-decoration:none}
.main-nav a.active{background:var(--plum-deep)}
.main-nav .search{padding:0 12px}
.hero{position:relative;height:220px;background:linear-gradient(180deg,#6d5c8a 0%,#9b8ba8 35%,#4a3a55 60%,#2f6f86 75%,#4aa6c2 88%,#2a2b33 100%)}
.hero-arrow{position:absolute;top:95px;width:24px;height:24px;border-radius:50%;background:rgba(255,255,255,.85);display:flex;align-items:center;justify-content:center}
.hero-arrow.prev{left:8px}.hero-arrow.next{right:8px}
.booking{background:var(--plum-dark);height:90px;padding:10px 50px 0;color:var(--white)}
.booking-fields{display:flex;gap:14px}
.field label{display:block;font-size:7.5px;margin-bottom:4px}
.field .row{display:flex;gap:4px;align-items:center}
.select{background:var(--white);color:#444;height:14px;font-size:6.5px;padding:2px 4px;border-radius:1px}
.cal{width:10px;height:11px;background:#ddd;border-radius:1px}
.opts{display:flex;gap:10px;font-size:6.5px;margin-top:5px}
.opts span::before{content:"";display:inline-block;width:6px;height:6px;background:var(--white);margin-right:3px;vertical-align:-1px}
.booking-btn{display:block;margin:10px auto 0;width:210px;height:18px;background:var(--plum);color:var(--white);font-size:7.5px;font-weight:600;text-align:center;line-height:18px;letter-spacing:.3px}
.welcome{height:190px;text-align:center;padding-top:28px}
.welcome h1{font-size:18px;font-weight:600;color:var(--ink)}
.welcome .tagline{font-size:9px;margin:6px 0 6px}
.welcome p{width:380px;margin:0 auto;font-size:7.5px;color:var(--muted);line-height:1.45}
.btn-dark{display:inline-block;margin-top:12px;background:var(--ink);color:var(--white);font-size:7px;font-weight:700;padding:4px 14px}
.features{background:var(--band);height:280px;display:flex;justify-content:center;gap:18px;padding-top:16px}
.card{width:170px;background:var(--white);border-top:5px solid}
.card.hotels{border-color:var(--green)}.card.rooms{border-color:var(--orange)}.card.restaurants{border-color:var(--blue)}
.card h2{font-size:15px;font-weight:400;padding:8px 10px;letter-spacing:.5px}
.card .photo{height:120px}
.card h3{font-size:8px;font-weight:600;padding:8px 10px 3px}
.card p{font-size:7px;color:var(--muted);padding:0 10px;line-height:1.4}
.card .more{display:inline-block;margin:8px 10px;color:var(--white);font-size:6.5px;font-weight:700;padding:3px 8px}
.hotels .more{background:var(--green)}.rooms .more{background:var(--orange)}.restaurants .more{background:var(--blue)}
.services{height:135px;padding:16px 60px 0}
.services h2{font-size:15px;font-weight:400;margin-bottom:14px}
.service-list{display:flex;gap:22px}
.service{display:flex;gap:10px;width:175px}
.service svg{flex:0 0 32px}
.service h3{font-size:8px;font-weight:600;line-height:1.3;margin-bottom:4px}
.service p{font-size:6.8px;color:var(--muted);line-height:1.4}
.gallery{height:185px;padding:14px 0 0;background:linear-gradient(120deg,#4b1a3c,#7a2d55 55%,#3a1230)}
.gallery h2{color:var(--white);font-size:15px;font-weight:400;padding-left:10px;margin-bottom:14px}
.thumbs{display:flex;gap:5px;justify-content:center}
.thumb{width:86px;height:86px;border:3px solid var(--white);position:relative}
.thumb.wide{width:86px}
.zoom{position:absolute;inset:0;display:flex;align-items:center;justify-content:center}
.zoom span{width:34px;height:34px;border-radius:50%;background:rgba(255,255,255,.25);display:flex;align-items:center;justify-content:center}
.dots{display:flex;gap:5px;justify-content:center;margin-top:10px}
.dots i{width:7px;height:7px;border-radius:50%;border:1px solid var(--white)}
.dots i.on{background:var(--white)}
.site-footer{height:50px;display:flex;align-items:center;justify-content:space-between;padding:0 34px;font-size:6.5px;color:#555}
.footer-links{display:flex;gap:9px}
.social{display:flex;gap:6px}
.social i{width:14px;height:14px;border-radius:2px}
</style>
</head>
<body>
<header class="site-header">
  <div class="brand">Le Mas des Ormeaux</div>
  <nav class="main-nav">
    <a class="active">Home</a><a>Photos</a><a>Price</a><a>Booking</a><a>Country Activities</a><a>City Activities</a><a>Map</a><a>Contact</a>
    <a class="search"><svg width="10" height="10" viewBox="0 0 10 10"><circle cx="4" cy="4" r="3" fill="none" stroke="#fff" stroke-width="1.3"/><line x1="6.3" y1="6.3" x2="9.3" y2="9.3" stroke="#fff" stroke-width="1.3"/></svg></a>
  </nav>
</header>

<section class="hero" role="img" aria-label="Evening view of the gîte terrace with a lit swimming pool and potted plants">
  <span class="hero-arrow prev"><svg width="8" height="10"><path d="M6 1 2 5l4 4" fill="none" stroke="#5e1a4d" stroke-width="1.6"/></svg></span>
  <span class="hero-arrow next"><svg width="8" height="10"><path d="M2 1l4 4-4 4" fill="none" stroke="#5e1a4d" stroke-width="1.6"/></svg></span>
</section>

<section class="booking">
  <div class="booking-fields">
    <div class="field"><label>Destinations / Hotel Name</label><div class="row"><span class="select" style="width:110px">Mulhouse</span></div>
      <div class="opts"><span>Gîtes</span><span>Rooms</span></div></div>
    <div class="field"><label>Check-in Date</label><div class="row"><span class="select" style="width:34px">Day</span><span class="select" style="width:58px">Month</span><span class="cal"></span></div></div>
    <div class="field"><label>Check-out Date</label><div class="row"><span class="select" style="width:34px">Day</span><span class="select" style="width:58px">Month</span><span class="cal"></span></div>
      <div class="opts"><span>I have specific dates</span></div></div>
    <div class="field"><label>Guests</label><div class="row"><span class="select" style="width:60px">1 Adult</span></div></div>
  </div>
  <span class="booking-btn">SEARCH YOUR GÎTE</span>
</section>

<section class="welcome">
  <h1>Welcome !</h1>
  <div class="tagline">" Luxury accommodations, worldwide reputation "</div>
  <p>Set among orchards near the German and Swiss borders, our gîte offers five quiet rooms, generous breakfasts and easy access to the city and the countryside alike.</p>
  <span class="btn-dark">MORE</span>
</section>

<section class="features">
  <article class="card hotels">
    <h2>HOTELS</h2>
    <div class="photo" role="img" aria-label="Wooden pier leading to overwater huts" style="background:linear-gradient(180deg,#6fa7cf,#9cc6d8 45%,#7a5a3a 75%,#4a3a2a)"></div>
    <h3>Charming village stays nearby</h3>
    <p>Quiet nights, warm welcome and breakfast served daily.</p>
    <span class="more">MORE</span>
  </article>
  <article class="card rooms">
    <h2>ROOMS</h2>
    <div class="photo" role="img" aria-label="Bright bedroom with white bedding" style="background:linear-gradient(180deg,#d8dde0,#f2f2f0 50%,#a8a59e)"></div>
    <h3>Five rooms, each its own</h3>
    <p>Bright, calm rooms with garden or village views.</p>
    <span class="more">MORE</span>
  </article>
  <article class="card restaurants">
    <h2>RESTAURANTS</h2>
    <div class="photo" role="img" aria-label="Restaurant dining room with set tables" style="background:linear-gradient(180deg,#5e8a4a,#cfd6c8 45%,#3a3a3a)"></div>
    <h3>Local tables worth the trip</h3>
    <p>Alsatian cuisine and wine only minutes away.</p>
    <span class="more">MORE</span>
  </article>
</section>

<section class="services">
  <h2>Our Services</h2>
  <div class="service-list">
    <div class="service">
      <svg width="32" height="32" viewBox="0 0 32 32"><path d="M6 20h20v3a6 6 0 0 1-6 6h-8a6 6 0 0 1-6-6z" fill="#222"/><path d="M10 17c0-4 12-4 12 0" fill="none" stroke="#222" stroke-width="2"/><rect x="15" y="9" width="2" height="5" fill="#222"/></svg>
      <div><h3>Breakfast served each morning</h3><p>Fresh bread, jam and fruit from nearby farms.</p></div>
    </div>
    <div class="service">
      <svg width="32" height="32" viewBox="0 0 32 32"><path d="M9 4h4v6l2 4v15H7V14l2-4z" fill="#222"/><path d="M19 6h8c0 6-1 9-4 9s-4-3-4-9z" fill="#222"/><rect x="22" y="15" width="2" height="10" fill="#222"/><rect x="19" y="25" width="8" height="2" fill="#222"/></svg>
      <div><h3>Regional wines at the table</h3><p>A small cellar of local bottles to discover.</p></div>
    </div>
    <div class="service">
      <svg width="32" height="32" viewBox="0 0 32 32"><circle cx="16" cy="17" r="9" fill="none" stroke="#222" stroke-width="2"/><circle cx="16" cy="17" r="5" fill="#222"/><path d="M3 5v9h2v14h2V14h1V5" fill="#222"/><path d="M27 5c-2 2-2 7 0 9v14h2V5z" fill="#222"/></svg>
      <div><h3>Meals prepared on request</h3><p>Dinners by arrangement with seasonal produce.</p></div>
    </div>
  </div>
</section>

<section class="gallery">
  <h2>Gallery</h2>
  <div class="thumbs">
    <div class="thumb" role="img" aria-label="Plated dish on a dark table" style="background:linear-gradient(160deg,#6a6a6a,#2a2a2a)">
      <div class="zoom"><span><svg width="14" height="14" viewBox="0 0 14 14"><circle cx="6" cy="6" r="4.5" fill="none" stroke="#fff" stroke-width="1.6"/><line x1="9.3" y1="9.3" x2="13" y2="13" stroke="#fff" stroke-width="1.8"/></svg></span></div>
    </div>
    <div class="thumb" role="img" aria-label="Lounge with sofa and windows" style="background:linear-gradient(160deg,#c8d8e0,#7f96a0)"></div>
    <div class="thumb" role="img" aria-label="Bedroom with red walls" style="background:linear-gradient(160deg,#d04a6a,#8a1e3a)"></div>
    <div class="thumb" role="img" aria-label="Contemporary living room" style="background:linear-gradient(160deg,#b8b0a6,#5a544e)"></div>
  </div>
  <div class="dots"><i class="on"></i><i></i><i></i></div>
</section>

<footer class="site-footer">
  <nav class="footer-links"><span>HOME</span><span>ABOUT US</span><span>BOOKING</span><span>LATEST NEWS</span><span>CONTACTS</span></nav>
  <div class="social"><i style="background:#3b5998"></i><i style="background:#c0392b"></i><i style="background:#2aa3d8"></i></div>
  <span>LE MAS DES ORMEAUX © 2015 PRIVACY POLICY</span>
</footer>
</body>
</html>
```